I need a logo that demonstrates multiple of the same with one of a distinguishing feature. I would like something that can be recognisable in silhouette format. The business designs Management systems bespoke the to the company helping them pre-qualify for work.
Something that can demonstrate a distinction between a collective group non of which are the same in shape or size, with the largest of these not the distinguished object (or something to that effect).
This is a new business no logo or artwork exists.
Target Market(s)
Small to Medium Size enterprises in the city and rural areas. Looking to make the step up.
Industry/Entity Type
Manufacture
Contact Information for Business Card
room for, Name, Email, phone number
Font styles to use
Requirements
Must have
- would like the silhouette to be recognisable
Nice to have
- would like it to incorporate the name Clearpath Advisory Group.
- Would like the same logo to be on both business cards and on corporate shirts
Should not have
- anything that may exclude rural trade or manufacturing.
- I don't want to appear as corporate, just professional

```html
<!DOCTYPE html>
<html lang="en">
<head>
<meta charset="utf-8">
<title>Clearpath Advisory Group — Business Cards</title>
<link href="https://fonts.googleapis.com/css2?family=Lato:wght@400;700&display=swap" rel="stylesheet">
<style>
  :root {
    --brand-red: #ec1c24;
    --accent-orange: #f26522;
    --paper-white: #ffffff;
    --paper-grey: #ececec;
    --backdrop: #efece8;
    --text-font: "Lato", Arial, sans-serif;
  }
  * { box-sizing: border-box; margin: 0; padding: 0; }
  html, body {
    width: 1200px; height: 900px; overflow: hidden;
    background: var(--backdrop);
    font-family: var(--text-font);
  }
  .stage {
    position: relative; width: 1200px; height: 900px;
    display: flex; flex-direction: column; align-items: center; justify-content: center; gap: 50px;
  }
  .card {
    position: relative; width: 580px; height: 330px; overflow: hidden;
    box-shadow: 0 6px 18px rgba(0,0,0,0.18);
  }

  /* Front */
  .card--front { background: var(--brand-red); display: flex; align-items: center; justify-content: center; }
  .wordmark { display: flex; align-items: center; gap: 18px; }
  .wordmark__dot {
    width: 78px; height: 78px; border-radius: 50%;
    border: 3px solid currentColor; flex: none;
  }
  .wordmark__name {
    font-weight: 400; font-size: 30px; line-height: 1.1; letter-spacing: 1px; text-transform: uppercase;
  }
  .card--front .wordmark { color: var(--paper-white); }

  /* Back */
  .card--back { background: var(--brand-red); }
  .back__header {
    position: absolute; left: 0; top: 0; width: 100%; height: 150px;
    background: linear-gradient(180deg, var(--paper-white) 0%, var(--paper-grey) 100%);
    display: flex; align-items: center; justify-content: center;
  }
  .card--back .wordmark { color: var(--brand-red); }
  .back__rule {
    position: absolute; left: 0; top: 150px; width: 100%; height: 16px;
    background: var(--paper-white);
    border-top: 4px solid var(--accent-orange);
  }
  .back__rule::after {
    content: ""; position: absolute; left: 0; bottom: 0; width: 100%; height: 4px;
    background: var(--accent-orange);
  }
  .back__details {
    position: absolute; left: 0; top: 166px; width: 100%; height: 164px;
    display: flex; align-items: center; color: var(--paper-white);
  }
  .person { width: 52%; text-align: right; padding-right: 28px; }
  .person__name { font-weight: 700; font-size: 22px; }
  .person__role { font-size: 15px; margin-top: 2px; }
  .person__address { font-size: 15px; margin-top: 12px; line-height: 1.35; }
  .contacts { list-style: none; font-size: 14px; }
  .contacts li { display: flex; align-items: center; gap: 8px; margin: 4px 0; }
  .contacts svg { width: 16px; height: 16px; flex: none; }
</style>
</head>
<body>
<main class="stage">

  <section class="card card--front" aria-label="Business card front">
    <div class="wordmark">
      <span class="wordmark__dot"></span>
      <span class="wordmark__name">Clearpath<br>Advisory Group</span>
    </div>
  </section>

  <section class="card card--back" aria-label="Business card back">
    <div class="back__header">
      <div class="wordmark">
        <span class="wordmark__dot"></span>
        <span class="wordmark__name">Clearpath<br>Advisory Group</span>
      </div>
    </div>
    <div class="back__rule"></div>
    <div class="back__details">
      <div class="person">
        <p class="person__name">Daniel Hart</p>
        <p class="person__role">Managing Director</p>
        <p class="person__address">48 Mill Lane, Northfield<br>Yorkshire, 20417</p>
      </div>
      <ul class="contacts">
        <li>
          <svg viewBox="0 0 16 16" aria-hidden="true"><rect width="16" height="16" rx="2" fill="#fff"/><path d="M4 5c0-1 1-1.5 4-1.5S12 4 12 5v1H10V5H6v1H4z M5 7h6l1 5H4z" fill="var(--brand-red)"/></svg>
          555-201-4870
        </li>
        <li>
          <svg viewBox="0 0 16 16" aria-hidden="true"><rect width="16" height="16" rx="2" fill="#fff"/><rect x="5" y="3" width="6" height="4" fill="var(--brand-red)"/><rect x="3" y="7" width="10" height="4" fill="var(--brand-red)"/><rect x="5" y="10" width="6" height="3" fill="var(--brand-red)"/></svg>
          555-201-4871
        </li>
        <li>
          <svg viewBox="0 0 16 16" aria-hidden="true"><rect width="16" height="16" rx="2" fill="#fff"/><rect x="3" y="5" width="10" height="7" fill="var(--brand-red)"/><path d="M3 5l5 4 5-4" stroke="#fff" stroke-width="1" fill="none"/></svg>
          hello@clearpathadvisory.com
        </li>
        <li>
          <svg viewBox="0 0 16 16" aria-hidden="true"><rect width="16" height="16" rx="2" fill="#fff"/><path d="M6 10l4-4M7 5.5l1-1a2 2 0 013 3l-1 1M9 10.5l-1 1a2 2 0 01-3-3l1-1" stroke="var(--brand-red)" stroke-width="1.4" fill="none" stroke-linecap="round"/></svg>
          www.clearpathadvisory.com
        </li>
      </ul>
    </div>
  </section>

</main>
</body>
</html>
```